Health care finance company startup website design

This design brief is for Ledger Loom, a small start-up company dealing with an online health care (initially dental targeted with plans for medical market) financial suite of tools. My business partners and I are looking to have a website developed for our business model.

We have developed a professional logo and would like it incorporated into the site. We are open to modifications on the logo if needed to accomplish the right design.

Our concept is a clean, simple design with a professional polish and very up-to-date web presence. The functionality of the site is simple yet powerful and we would like it’s design to complement that (including anticipated css3/html5 effects for an added dimension of UI polish).

We would like to see a design mockup of the functional elements of our site as our home page. We would also be very interested to see how your design would flow into the other pages such as search for a loan, create a payment plan, make a payment, sign in, registration, contact us and learn more.

Regarding Functional Elements:

-Simplicity is king.

-The three main functions of the site are the focus. They will operate via a series of API’s to webservices on the back-end, making the front end field focused, though we hope to have it feel friendly and simple.
-Search for a loan
-Create a payment plan
-Make a payment

Other functions of the site include:

-Sign in module
-We plan to support Kindred Link, Vortal Verify and PassGate so incorporating design for those options is a plus.

-Registration module
-Two service levels clients can register for, loans only or loans & payments
-The registration process should be divided into sections with navigation back and forth until a confirmation final screen with pdf generations and remaining “to-do items” listed.
-The registration information will be saved in our database and also auto-populate fields for PDF’s that will be generated from templates.
-The registration will send a confirmation email and support PassGate, Vortal Verify and Kindred Link, so designs should take these programmatic features into account.

-Contact us
-This will emphasize digital forms of communication (email and form submitted contact request).

-Learn more
-Explanations/faqs/tutorials
-This will contain video demonstrations/screencasts of key functions of website features

Regarding Design Elements:
-We want to be “wow’d” and don’t mind a surprise that redefines what we thought we liked regarding design.
-The following examples indicate some of the color schemes we like and design elements we hope to incorporate.
-We also recognize there is no substitute for creativity and originality.

Favorite Website Design Examples:

http://www.joggingwithmarla.example/
HD backgrounds are a plus.
These colors are great.
The bright splashes of blue, red and orange combined with black in these shades.
A predominant background of whitesmoke or beige.

https://tillbrook.example/
The HD backgrounds are sharp.
The look is very clean (though it has a slight Pearfield computers imitation).
The left to right “scrolling” is preferable to vertical scrolling.
Very pleasing to the eye.

http://www.gravelpathworks.example/
Again, use of bright, vibrant HD graphics is exceptional.
The left to right scrolling navigation is slick and likely how we would like our services to flow.

http://buzzing.visitlakeshore.example/
Love the look, feel and concepts in this site’s design
Especially colors and “photography” elements.
Updates

We've seen a few common themes in various designs submitted so far and want to add a few suggestions as we enter the final week of our design contest.

We do not want any photos of healthcare professionals or close-ups of people (families or couples or individuals).  Although we are a health care company we don't want to fall into a cliche feel for our site.  Instead we would like either objects or abstract images that have depth and are high definition, spanning from edge to edge of the width of the screen. 

We prefer shades of grey for the base color scheme with highlights of bright colors.  Please refer to the examples on the brief and use those as the best guide of what we want.  Even SketchHive's color scheme is closer to what we want than some of the submissions, so please take note of the "shades of grey" with splashes of bright accent colors.

We love the horizontal navigation bar like that seen in the gravel-path works site and anticipate our final product using a similar transition between the functions of the site.

Good luck to you all.  We are still looking for that WOW factor and hoping to see something original, that breaks the traditional mold and has a feel like the examples posted.  

Industry/Entity Type

Communication

```html
<!DOCTYPE html>
<html lang="en">
<head>
<meta charset="utf-8">
<title>Health Care</title>
<link rel="stylesheet" href="https://fonts.googleapis.com/css2?family=Roboto+Condensed:wght@700&family=Source+Sans+3:wght@400;600&family=Arimo:ital,wght@0,400;0,700;1,400&display=swap">
<style>
:root{
  --red:#c8202a;
  --red-dark:#a3161e;
  --orange:#f08a4b;
  --yellow:#f4b942;
  --ink:#333;
  --muted:#888;
  --page:#f3f0eb;
  --panel:#f8f7f4;
  --line:#dcd8d2;
  --white:#fff;
}
*{margin:0;padding:0;box-sizing:border-box}
html,body{width:968px;height:1200px;overflow:hidden}
body{position:relative;background:var(--page);font-family:"Arimo",Arial,sans-serif;color:var(--ink)}
.abs{position:absolute}
.top-bar{left:0;top:0;width:968px;height:7px;background:var(--red)}
.header{left:0;top:7px;width:968px;height:86px;background:var(--panel);border-bottom:1px solid var(--line)}
.brand{left:80px;top:37px;display:flex;align-items:center;gap:8px;font-family:"Roboto Condensed",sans-serif;font-size:36px;color:#222;line-height:1}
.brand-square{width:18px;height:18px;background:var(--red)}
.account{top:7px;height:19px;font-size:10px;font-weight:700;color:var(--white);display:flex;align-items:center;justify-content:center}
.account.social{left:662px;width:124px;background:#3b4f80;font-weight:400}
.account.login{left:790px;width:40px;background:var(--red)}
.account.signup{left:834px;width:53px;background:var(--red-dark)}
.nav{top:47px;left:509px;display:flex;font-family:"Source Sans 3",sans-serif;font-size:13.5px}
.nav a{color:#333;text-decoration:none;height:24px;line-height:24px;margin-right:18px}
.nav a.current{background:var(--red);color:var(--white);padding:0 17px;font-weight:600;border-top:2px solid #e24a52}
.hero{left:0;top:93px;width:968px;height:401px;background:linear-gradient(90deg,#c9d7e4 0%,#e9ecef 30%,#c8c2bc 60%,#e6e2dc 100%)}
.callout-title{left:430px;top:223px;width:457px;height:69px;background:var(--white);padding:9px 16px;font-family:"Source Sans 3",sans-serif;font-size:19px;line-height:25px;color:#444;box-shadow:0 2px 4px rgba(0,0,0,.15)}
.callout-body{left:430px;top:292px;width:457px;height:105px;background:var(--red);padding:18px 16px;font-size:11px;font-weight:700;line-height:16.5px;color:var(--white);text-align:justify}
.callout-tail{left:462px;top:396px}
.slider-band{left:0;top:494px;width:968px;height:56px;background:var(--panel);border-bottom:1px solid var(--line)}
.dot{top:517px;width:12px;height:12px;border-radius:50%;background:var(--red)}
.dot.active{background:#444;width:15px;height:15px;top:515px}
.tile{top:550px;height:97px;padding:16px 0 0 86px;color:var(--white)}
.tile h3{font-family:"Source Sans 3",sans-serif;font-weight:400;font-size:18px;margin-bottom:5px}
.tile p{font-size:10px;line-height:13px;width:170px}
.tile svg{position:absolute;left:16px;top:14px}
.tile.loan{left:82px;width:269px;background:var(--orange)}
.tile.loan h3{color:#b14a16}
.tile.plan{left:351px;width:270px;background:var(--yellow)}
.tile.plan h3{color:#b7741a}
.tile.pay{left:621px;width:266px;background:var(--red)}
.tile.pay h3{color:#7a0e14}
.section-title{font-family:"Source Sans 3",sans-serif;font-weight:600;font-size:19px;color:#333}
.section-title span{color:var(--red)}
.welcome-photo{left:97px;top:723px;width:235px;height:139px;background:linear-gradient(135deg,#6fa3a6,#c7dedc 55%,#e8c9b6)}
.body-text{font-size:10px;line-height:13px;color:#666;text-align:justify}
.divider{left:351px;top:678px;width:1px;height:338px;background:var(--line)}
.quote-head{left:378px;top:730px;width:497px;display:flex;justify-content:space-between;font-size:11px;border-bottom:1px solid var(--line);padding-bottom:6px}
.quote-head b span{color:var(--red)}
.quote-head i{font-size:9.5px;color:#777}
.quote-text{left:378px;top:758px;width:497px;font-size:9.5px;line-height:13px;font-style:italic;color:#777}
.quote-rule{left:378px;top:826px;width:497px;height:1px;background:var(--line)}
.mini-dot{top:840px;width:5px;height:5px;border-radius:50%;background:#aaa}
.btn-red{background:var(--red);color:var(--white);font-size:10px;display:flex;align-items:center;justify-content:center;border-radius:2px}
.partners{left:371px;top:914px;width:506px;height:86px;background:var(--white);border:1px solid var(--line);border-radius:4px}
.partner-badge{top:944px;height:26px;background:#d9d6d2;border-radius:3px}
.footer{left:0;top:1055px;width:968px;height:134px;background:var(--panel);border-top:1px solid var(--line)}
.footer h4{font-family:"Source Sans 3",sans-serif;font-weight:400;font-size:14px;color:#333}
.footer-links{font-size:9.5px;line-height:16px;color:#555;list-style:none}
.email-field{left:328px;top:1105px;width:229px;height:22px;background:var(--white);border:1px solid #ccc;font-size:9.5px;font-style:italic;color:#888;padding:5px 8px}
.footer-brand{left:673px;top:1083px;display:flex;align-items:center;gap:8px;font-family:"Roboto Condensed",sans-serif;font-size:36px;color:#e8cfcf;line-height:1}
.footer-brand .brand-square{background:#efc6c6}
.bottom-bar{left:0;top:1189px;width:968px;height:11px;background:var(--red)}
</style>
</head>
<body>
<div class="abs top-bar"></div>
<header class="abs header"></header>
<div class="abs brand"><span class="brand-square"></span>Health Care</div>
<div class="abs account social">Connect with Kindred Link</div>
<div class="abs account login">Login</div>
<div class="abs account signup">Sign Up</div>
<nav class="abs nav"><a class="current">Home</a><a>About Us</a><a>Payment Plan</a><a>Partners</a><a>Contact Us</a></nav>

<div class="abs hero" role="img" aria-label="Wide hero photograph of a smiling clinician in a bright hospital setting"></div>
<div class="abs callout-title">Lorem Ipsum is simply dummy text of the Printing and typesetting industry.</div>
<div class="abs callout-body">Lorem Ipsum is simply dummy text of the printing and typesetting industry. Lorem Ipsum has been the industry's standard dummy text ever since the 1500s, when an unknown printer took a galley of type and scrambled it to make a type specimen book. It has survived not only five centuries,</div>
<svg class="abs callout-tail" width="36" height="20" viewBox="0 0 36 20"><path d="M0 0H36L6 18Z" fill="var(--red)"/></svg>

<div class="abs slider-band"></div>
<div class="abs dot" style="left:457px"></div>
<div class="abs dot active" style="left:476px"></div>
<div class="abs dot" style="left:499px"></div>
<div class="abs dot" style="left:517px"></div>

<div class="abs tile loan">
  <svg width="56" height="60" viewBox="0 0 56 60"><circle cx="24" cy="22" r="15" fill="none" stroke="#fff" stroke-width="6"/><path d="M35 33L50 52" stroke="#fff" stroke-width="9" stroke-linecap="round"/></svg>
  <h3>Search For a Loan</h3><p>Lorem Ipsum is simply dummy text of the printing and typesetting industry.</p>
</div>
<div class="abs tile plan">
  <svg width="56" height="60" viewBox="0 0 56 60"><rect x="2" y="8" width="44" height="30" rx="2" fill="#e39a24" stroke="#fff" stroke-width="3"/><rect x="10" y="20" width="44" height="30" rx="2" fill="#fff"/><rect x="10" y="26" width="44" height="5" fill="#e39a24"/><rect x="16" y="38" width="18" height="3" fill="#e39a24"/></svg>
  <h3>Create a Payment Plan</h3><p>Lorem Ipsum is simply dummy text of the printing and typesetting industry.</p>
</div>
<div class="abs tile pay">
  <svg width="56" height="60" viewBox="0 0 56 60"><circle cx="26" cy="28" r="24" fill="#fff"/><circle cx="26" cy="28" r="18" fill="var(--red)"/><text x="26" y="38" text-anchor="middle" font-family="Arimo,sans-serif" font-weight="700" font-size="27" fill="#fff">$</text></svg>
  <h3>Make a Payment</h3><p>Lorem Ipsum is simply dummy text of the printing and typesetting industry.</p>
</div>

<h2 class="abs section-title" style="left:94px;top:687px">Welcome to <span>Health Care</span></h2>
<div class="abs welcome-photo" role="img" aria-label="Photograph of a dental check-up in a treatment room"></div>
<p class="abs body-text" style="left:97px;top:869px;width:236px">Lorem ipsum dolor sit amet, consectetur adipiscing elit. Sed posuere diam quis turpis varius fermentum in in ipsum. Morbi eget quam vitae nisl consectetur sodales facilisis at ipsum. Sed id justo libero. Sed vestibulum tincidunt ultrices. Duis accumsan velit porttitor ipsum fringilla pretium.</p>
<p class="abs body-text" style="left:97px;top:959px;width:236px">Pellentesque faucibus aliquet consectetur. Ut tempor bibendum rutrum. Mauris ut neque et lacus fringilla ulla-mcorper dignissim in sem.</p>

<div class="abs divider"></div>

<h2 class="abs section-title" style="left:371px;top:687px">What Our <span>Customers Say</span></h2>
<div class="abs quote-head"><b>Elias Moreno, <span>Manager.</span></b><i>Posted : 27 Jan, 2012 &nbsp; | &nbsp; 20:15 am</i></div>
<p class="abs quote-text">Lorem ipsum dolor sit amet, consectetur adipiscing elit. Sed posuere diam quis turpis varius fermentum in in ipsum. Morbi eget quam vitae nisl consectetur sodales facilisis at ipsum. Sed id justo libero. Sed vestibulum tincidunt ultrices. Duis accumsan velit porttitor ipsum fringilla pretium. Pellentesque faucibus aliquet consectetur. Ut tempor bibendum rutrum. Mauris ut neque et lacus fringilla ullamcorper dignissim in sem.</p>
<div class="abs quote-rule"></div>
<div class="abs mini-dot" style="left:379px;background:var(--red)"></div>
<div class="abs mini-dot" style="left:387px"></div>
<div class="abs mini-dot" style="left:395px"></div>
<div class="abs mini-dot" style="left:403px"></div>
<div class="abs mini-dot" style="left:411px"></div>
<div class="abs btn-red" style="left:768px;top:831px;width:101px;height:18px">view all testimonials</div>

<h2 class="abs section-title" style="left:371px;top:878px">Our <span>Business Partners</span></h2>
<div class="abs partners"></div>
<svg class="abs" style="left:376px;top:948px" width="18" height="18" viewBox="0 0 18 18"><circle cx="9" cy="9" r="9" fill="#222"/><path d="M11 5L7 9L11 13" stroke="#fff" stroke-width="2" fill="none"/></svg>
<svg class="abs" style="left:855px;top:948px" width="18" height="18" viewBox="0 0 18 18"><circle cx="9" cy="9" r="9" fill="#222"/><path d="M7 5L11 9L7 13" stroke="#fff" stroke-width="2" fill="none"/></svg>
<div class="abs partner-badge" style="left:404px;width:76px"></div>
<div class="abs partner-badge" style="left:522px;width:74px"></div>
<div class="abs partner-badge" style="left:616px;width:94px"></div>
<div class="abs partner-badge" style="left:758px;width:80px"></div>

<footer class="abs footer"></footer>
<h4 class="abs" style="left:95px;top:1078px;font-family:'Source Sans 3',sans-serif;font-weight:400;font-size:14px">About Us</h4>
<ul class="abs footer-links" style="left:95px;top:1102px"><li>Company Info</li><li>Search Loan</li><li>Services</li><li>Clients</li></ul>
<ul class="abs footer-links" style="left:196px;top:1102px"><li>Payment Plan</li><li>Partners</li><li>Contact Us</li><li>Terms &amp; Privacy</li></ul>
<h4 class="abs" style="left:329px;top:1078px;font-family:'Source Sans 3',sans-serif;font-weight:400;font-size:14px">Subscribe Newsletter</h4>
<div class="abs email-field">Email Address</div>
<div class="abs btn-red" style="left:328px;top:1137px;width:102px;height:23px;font-size:11px">Subscribe Now</div>
<p class="abs" style="left:436px;top:1137px;width:120px;font-size:9px;line-height:13px;color:#666">Free Subscribe our latest offers and Plans.</p>
<div class="abs footer-brand"><span class="brand-square"></span>Health Care</div>
<p class="abs" style="left:700px;top:1139px;width:185px;text-align:right;font-size:9px;color:#666">Copy © Health Care. All rights reserved.</p>
<div class="abs bottom-bar"></div>
</body>
</html>
```